Esoteric, wellness company labels

Verdant Lumen is a lifestyle brand with multiple products. We have an offshoot as well called Lumen Coffee. I need multiple labels or packaging designs that all match so I can start wholesaling.

I want something fun and very eye catching. I have two different logos for Verdant Lumen but just one for the coffee. I’m
Undecided which one I want on the labels because I like both. So either would work. Any coffee products go under lumen coffee and any other products go under Verdant Lumen.

We sell items such as crystals, tarot and oracle decks, candles, organic coffee, superfood powders and herbs and more.

The items I need labels for should have a streamline look so that all are recognizable as the Verdant Lumen brand. The products that are a priority are:
Organic coffee
Reishi infused coffee
Lion’s Mane infused coffee
Those go under Lumen Coffee.

Soon I’ll do more items;
Sacred smudging spray
Sacred smudging cleaner
Multiple superfoods
Etc
Updates

We have decided to use compostable coffee bags that are approximately 9x6x33cm so your standard 1lb bag you would see in a store. We still want colorful and eye catching but at the same time being eco friendly. The coffee is 100% organic, free trade, low acid.

We are looking for labels for the coffee but also want to be able to use the same kind of design or similar down the road for our other products. We carry superfood powders (lion’s mane, blue Spirulina, reishi, pearl powder, sea moss etc) but also things like smudging spray, rose water, neroli water, essential oils etc. we are a lifestyle company so we are looking for labels across our store brand items.

Target Market(s)

Esoteric, health and wellness, “new age”

Industry/Entity Type

Retail, wellness,

Colors

Designer to choose colors to be used in the design.

Requirements
Must have
• Beauty, attraction
Should not have
• Anything to do with religion, no dark witchy themes

```html
<!DOCTYPE html>
<html lang="en">
<head>
<meta charset="utf-8">
<title>Lumen Coffee — Organic Coffee Label</title>
<link rel="stylesheet" href="https://fonts.googleapis.com/css2?family=Abril+Fatface&family=Cormorant+Garamond:wght@600&family=Oswald:wght@400&display=swap">
<style>
  :root {
    --paper: #ffffff;
    --label-sand: #ebcd8a;
    --arch-terracotta: #c96833;
    --arch-line: #f4cfba;
    --ink-navy: #18253a;
    --gold: #e6b536;
    --cream: #f6e9dc;
    --leaf-gold: #e9a828;
    --leaf-deep: #b8621c;
  }
  * { margin: 0; padding: 0; box-sizing: border-box; }
  html, body { width: 1200px; height: 1200px; overflow: hidden; background: var(--paper); }
  .canvas { position: relative; width: 1200px; height: 1200px; }
  .label-sheet {
    position: absolute; left: 339px; top: 198px; width: 534px; height: 801px;
    background: var(--label-sand);
  }
  .arch-art { position: absolute; left: 0; top: 0; width: 1200px; height: 1200px; }
  .arch-tagline {
    font-family: "Abril Fatface", serif; font-size: 23px; fill: var(--cream); letter-spacing: 0.3px;
  }
  .brand-mark {
    position: absolute; left: 581px; top: 300px; width: 52px; height: 52px;
    border-radius: 50%; background: var(--ink-navy);
  }
  .brand-name {
    position: absolute; left: 400px; width: 414px; top: 392px; text-align: center;
    font-family: "Abril Fatface", serif; font-size: 44px; line-height: 40px;
    color: var(--ink-navy); letter-spacing: 0.5px;
  }
  .parent-badge {
    position: absolute; left: 525px; top: 494px; width: 152px; height: 53px;
    border: 1.5px solid var(--ink-navy);
    display: flex; flex-direction: column; align-items: center; justify-content: center;
    font-family: "Cormorant Garamond", serif; font-weight: 600; font-size: 13px;
    line-height: 16px; letter-spacing: 5px; color: var(--ink-navy); padding-left: 5px;
  }
  .site-url {
    position: absolute; left: 450px; width: 314px; top: 565px; text-align: center;
    font-family: "Cormorant Garamond", serif; font-weight: 600; font-size: 7px;
    letter-spacing: 3px; color: var(--ink-navy);
  }
  .branch {
    position: absolute; top: 559px; width: 128px; height: 197px;
    background: radial-gradient(ellipse at 50% 45%, var(--leaf-gold) 0%, var(--leaf-deep) 70%, transparent 72%);
    opacity: 0.85;
  }
  .branch--left { left: 419px; }
  .branch--right { left: 666px; }
  .product-title {
    position: absolute; left: 400px; width: 414px; top: 580px; text-align: center;
    font-family: "Abril Fatface", serif; font-size: 78px; line-height: 62px; color: var(--gold);
  }
  .product-title span { display: block; }
  .spec-row {
    position: absolute; left: 400px; width: 414px; top: 757px;
    display: flex; justify-content: center; align-items: baseline; gap: 10px; color: var(--cream);
  }
  .spec-weight { font-family: "Oswald", sans-serif; font-size: 14px; }
  .spec-roast { font-family: "Abril Fatface", serif; font-size: 22px; letter-spacing: 0.5px; }
  .origin {
    position: absolute; left: 400px; width: 414px; top: 785px; text-align: center;
    font-family: "Abril Fatface", serif; font-size: 34px; color: var(--gold);
  }
  .format {
    position: absolute; left: 400px; width: 414px; top: 832px; text-align: center;
    font-family: "Abril Fatface", serif; font-size: 21px; line-height: 32px; color: var(--cream);
    letter-spacing: 0.5px;
  }
</style>
</head>
<body>
<main class="canvas">
  <div class="label-sheet"></div>

  <svg class="arch-art" viewBox="0 0 1200 1200" aria-hidden="true">
    <path fill="var(--arch-terracotta)"
      d="M404,440.5 A203.5,203.5 0 0 1 811,440.5 L811,879 Q811,924 766,924 L449,924 Q404,924 404,879 Z"/>
    <path fill="none" stroke="var(--arch-line)" stroke-width="2.5"
      d="M417.5,445 A190,190 0 0 1 797.5,445 L797.5,877 Q797.5,909 765.5,909 L449.5,909 Q417.5,909 417.5,877 Z"/>
    <defs>
      <path id="tagline-curve" d="M449,450 A158,158 0 0 1 765,450"/>
    </defs>
    <text class="arch-tagline">
      <textPath href="#tagline-curve" startOffset="50%" text-anchor="middle">The coffee is 100% organic, free trade, low acid</textPath>
    </text>
  </svg>

  <div class="brand-mark"></div>
  <h1 class="brand-name">LUMEN<br>COFFEE</h1>

  <div class="parent-badge"><span>VERDANT</span><span>LUMEN</span></div>
  <p class="site-url">VERDANTLUMEN.COM</p>

  <div class="branch branch--left" role="img" aria-label="Illustrated coffee branch with leaves, cherries and blossoms"></div>
  <div class="branch branch--right" role="img" aria-label="Illustrated coffee branch with leaves, cherries and blossoms"></div>

  <h2 class="product-title"><span>Organic</span><span>coffee</span></h2>

  <div class="spec-row">
    <span class="spec-weight">12 OZ</span>
    <span class="spec-roast">MEDIUM ROAST</span>
    <span class="spec-weight">340 G</span>
  </div>
  <p class="origin">ETHIOPIA</p>
  <p class="format">WHOLE BEAN<br>BLEND</p>
</main>
</body>
</html>
```